Stationery Design Project - Mark Delaveri

I have recently designed my personal logo - Mark Delaveri (here on pixelhive.com) and now i'm looking to complete my corporate identity, with adding:
- Business Card
- Letter Head
- Envelope
- Brochure template (that will be used to promote any of the workshops or other services I provide along with a short summary about my credentials, and testimonials) - you can take your pick from the website: http://markdelaveri.com

Refer to website for more insight into the brand and the look & feel

PS.
- PLEASE REFER TO ATTACHED FILE AND READ THE "SHOULD NOT HAVE SECTION OF THIS BRIEF"
- I have attached two vector files, displaying the logo alteration on two different backgrounds (dark & light)
Updates

ONLY 2 DAYS LEFT ON DEADLINE. KEEP THOSE DESIGNS COMING.

Target Market(s)

1) One-on-one Business Executive 2) Companies requesting my workshops for mid management teams & public speaking events like BRIM Forums

Industry/Entity Type

Business

Requirements
Must have
• - must fit the look and feel of the logo (notice that I have attached the logo, and an emblem)
- the final files should be ready for printing - with info on colours, sizes, bleed area, margins, UV spot (if applicable), suggested material to print on (applies to business cards in particular)
- brand guide lines should be laid out too (font, colour, etc ...)
Nice to have
• It would be nice to produce something different that your standard sizes & di-cut in terms of business card, and letter head ...
Should not have
• THE EMBLEM (MD) AND THE LOGO (MARK DELAVERI) SHOULD NOT BE LAYED OUT AS PER THE ATTACHED FILE - THEY SHOULD BE SEPARATED - THE EMBLEM (MD) CAN BE USED IN PARTIAL OR AS WATERMARK - BUT NOT THE LOGO (MARK DELAVERI)

```html
<!DOCTYPE html>
<html lang="en">
<head>
<meta charset="utf-8">
<title>Mark Delaveri – Stationery Set</title>
<link rel="stylesheet" href="https://fonts.googleapis.com/css2?family=Open+Sans:wght@400;600;700&family=Oswald:wght@500&family=Lora:ital@1&display=swap">
<style>
:root{
  --stage:#8a7155;
  --paper:#ffffff;
  --sky:#72c3ee;
  --sky-deep:#3aa3dc;
  --ink:#4a4a4a;
  --charcoal:#58585a;
  --steel-light:#cfcfcf;
  --steel-dark:#8e8e8e;
  --ghost:#ececec;
}
*{box-sizing:border-box;margin:0;padding:0}
html,body{width:1200px;height:960px;overflow:hidden}
body{background:var(--stage);font-family:"Open Sans",Arial,sans-serif;color:var(--ink);position:relative}
.sheet{position:absolute;background:var(--paper);overflow:hidden}
.wordmark{font-family:"Oswald",Arial,sans-serif;font-weight:500;color:var(--charcoal);letter-spacing:.3px;line-height:1;white-space:nowrap}
.tagline{font-family:"Open Sans",Arial,sans-serif;font-size:6px;letter-spacing:1px;color:var(--charcoal);text-transform:uppercase;border-top:1.5px solid var(--sky);padding-top:2px;margin-top:3px;text-align:center}
.emblem{position:absolute;border-radius:50%;display:flex;align-items:center;justify-content:center;font-family:"Open Sans",Arial,sans-serif;font-weight:700}
.emblem--ghost{border:10px solid var(--ghost);color:var(--ghost)}
.emblem--solid{background:var(--paper);color:var(--charcoal);border:3px solid var(--ghost)}
.contact{font-size:10px;line-height:14px;color:var(--ink)}
.contact-line{display:flex;align-items:center;gap:5px}
.icon{width:9px;height:9px;flex:none}
.web{font-weight:700;color:var(--ink)}
.stack-right{text-align:right}
.stack-right .contact-line{justify-content:flex-end}

/* Folder */
.folder{left:35px;top:25px;width:625px;height:465px}
.folder-art{position:absolute;left:0;top:0}
.folder .wordmark{position:absolute;right:34px;top:68px;font-size:30px}
.folder .quote{position:absolute;left:250px;top:150px;font-family:"Lora",Georgia,serif;font-style:italic;color:#fff;font-size:21px;line-height:27px}
.folder .quote-author{display:block;text-align:right;font-family:"Open Sans",Arial,sans-serif;font-size:6px;font-style:normal;margin-top:2px}
.folder .portrait{position:absolute;left:435px;top:160px;width:190px;height:190px}
.folder .contact{position:absolute;left:48px;top:383px}
.folder .web{position:absolute;right:62px;top:422px;font-size:12px}

/* Letterhead */
.letterhead{left:600px;top:52px;width:560px;height:678px}
.letterhead .wordmark{position:absolute;right:50px;top:42px;font-size:22px}
.letterhead .contact{position:absolute;right:56px;top:78px;font-size:8.5px;line-height:11px}
.letterhead .web{position:absolute;left:14px;top:596px;font-size:9px}

/* Envelope */
.envelope-back{left:35px;top:495px;width:575px;height:140px}
.envelope-front{left:25px;top:605px;width:587px;height:310px}
.envelope-front .wordmark{position:absolute;left:58px;top:190px;font-size:24px}
.envelope-front .contact{position:absolute;left:60px;top:226px;font-size:9.5px;line-height:13px}

/* Business cards */
.card-back{left:728px;top:605px;width:294px;height:165px;background:var(--charcoal)}
.card-back .web{position:absolute;left:0;right:0;top:140px;text-align:center;color:#fff;font-size:9px}
.card-front{left:778px;top:760px;width:297px;height:175px}
.card-front .wordmark{position:absolute;left:35px;top:48px;font-size:18px}
.card-front .holder{position:absolute;right:24px;top:52px;text-align:right}
.card-front .holder-name{color:var(--sky-deep);font-size:13px;line-height:15px}
.card-front .holder-role{font-size:10px}
.card-front .contact{position:absolute;right:30px;top:102px;font-size:8px;line-height:11px}
.card-front .web{position:absolute;left:24px;top:138px;font-size:8px}
</style>
</head>
<body>

<svg width="0" height="0" style="position:absolute" aria-hidden="true">
  <symbol id="i-home" viewBox="0 0 10 10"><rect width="10" height="10" fill="var(--charcoal)"/><path d="M5 2 8 5H7v3H3V5H2z" fill="#fff"/></symbol>
  <symbol id="i-phone" viewBox="0 0 10 10"><rect width="10" height="10" fill="var(--charcoal)"/><path d="M3 2h1.5l.5 2-1 .8a5 5 0 0 0 1.2 1.2l.8-1 2 .5V7.5L7 8C4.5 8 2 5.5 2 3z" fill="#fff"/></symbol>
  <symbol id="i-mail" viewBox="0 0 10 10"><rect width="10" height="10" fill="var(--charcoal)"/><rect x="2" y="3" width="6" height="4" fill="none" stroke="#fff" stroke-width=".8"/><path d="M2 3 5 5.5 8 3" fill="none" stroke="#fff" stroke-width=".8"/></symbol>
  <symbol id="i-home-sky" viewBox="0 0 10 10"><rect x=".5" y=".5" width="9" height="9" fill="none" stroke="var(--sky-deep)"/><path d="M5 2.5 7.5 5H7v2.5H3V5h-.5z" fill="var(--sky-deep)"/></symbol>
  <symbol id="i-phone-sky" viewBox="0 0 10 10"><rect x=".5" y=".5" width="9" height="9" fill="none" stroke="var(--sky-deep)"/><path d="M3 2.5h1.3l.4 1.7-.8.7a4.5 4.5 0 0 0 1.2 1.2l.7-.8 1.7.4V7L7 7.5C4.8 7.5 2.5 5.2 2.5 3z" fill="var(--sky-deep)"/></symbol>
  <symbol id="i-mail-sky" viewBox="0 0 10 10"><rect x=".5" y=".5" width="9" height="9" fill="none" stroke="var(--sky-deep)"/><rect x="2.5" y="3" width="5" height="4" fill="none" stroke="var(--sky-deep)" stroke-width=".8"/><path d="M2.5 3 5 5.2 7.5 3" fill="none" stroke="var(--sky-deep)" stroke-width=".8"/></symbol>
</svg>

<!-- Letterhead -->
<section class="sheet letterhead">
  <div class="emblem emblem--ghost" style="left:150px;top:210px;width:225px;height:225px;font-size:70px">MD</div>
  <div class="wordmark">MARK DELAVERI</div>
  <div class="contact stack-right">
    <div class="contact-line">Byblos - Lebanon <svg class="icon"><use href="#i-home-sky"/></svg></div>
    <div class="contact-line">P.O.Box 48-216 Jbeil <svg class="icon" style="visibility:hidden"><use href="#i-home-sky"/></svg></div>
    <div class="contact-line">00961 71 538209 <svg class="icon"><use href="#i-phone-sky"/></svg></div>
    <div class="contact-line">me@markdelaveri.com <svg class="icon"><use href="#i-mail-sky"/></svg></div>
  </div>
  <div class="web">www.markdelaveri.com</div>
</section>

<!-- Folder -->
<section class="sheet folder">
  <svg class="folder-art" width="625" height="465" viewBox="0 0 625 465">
    <defs>
      <linearGradient id="steel" x1="0" y1="0" x2="1" y2="1">
        <stop offset="0" stop-color="var(--steel-dark)"/>
        <stop offset=".5" stop-color="var(--steel-light)"/>
        <stop offset="1" stop-color="var(--steel-dark)"/>
      </linearGradient>
    </defs>
    <path d="M0 110 L625 150 V156 L0 116Z" fill="var(--sky)"/>
    <path d="M0 118 L625 158 V385 L0 350Z" fill="url(#steel)"/>
    <path d="M0 343 L625 378" stroke="var(--sky)" stroke-width="2"/>
    <path d="M0 350 L625 385 V465 H0Z" fill="var(--sky)"/>
  </svg>
  <div class="emblem emblem--ghost" style="left:75px;top:25px;width:80px;height:80px;border-width:5px;font-size:22px">MD</div>
  <div class="wordmark">MARK DELAVERI<div class="tagline">Lead with your own voice</div></div>
  <p class="quote">“Speak Up …<br>&nbsp;&nbsp;&nbsp;&nbsp;&nbsp;&nbsp;&nbsp;&nbsp;Stand Out!”<span class="quote-author">Mark Delaveri</span></p>
  <div class="portrait" role="img" aria-label="Black and white portrait of Mark Delaveri in a dark jacket" style="background:linear-gradient(180deg,#b8b8b8,#606060);clip-path:polygon(0 0,100% 0,100% 100%,0 88%)"></div>
  <div class="emblem emblem--solid" style="left:568px;top:350px;width:36px;height:36px;font-size:11px">MD</div>
  <div class="contact">
    <div class="contact-line"><svg class="icon"><use href="#i-home"/></svg>Byblos - Lebanon, P.O.Box 48-216 Jbeil</div>
    <div class="contact-line"><svg class="icon"><use href="#i-phone"/></svg>00961 71 538209 <svg class="icon"><use href="#i-mail"/></svg>me@markdelaveri.com</div>
  </div>
  <div class="web">www.markdelaveri.com</div>
</section>

<!-- Envelope back flap -->
<section class="sheet envelope-back">
  <svg width="575" height="140" viewBox="0 0 575 140" style="position:absolute;left:0;top:0">
    <path d="M0 0 H575 L548 80 H25Z" fill="var(--sky)"/>
  </svg>
  <div class="emblem emblem--solid" style="left:260px;top:12px;width:55px;height:55px;font-size:16px">MD</div>
</section>

<!-- Envelope front -->
<section class="sheet envelope-front">
  <div class="emblem emblem--ghost" style="left:75px;top:55px;width:100px;height:100px;font-size:28px">MD</div>
  <svg width="587" height="310" viewBox="0 0 587 310" style="position:absolute;left:0;top:0">
    <path d="M0 290 L587 245 V250 L0 295Z" fill="var(--sky)"/>
    <path d="M0 298 L587 258 V310 H0Z" fill="var(--sky)"/>
  </svg>
  <div class="wordmark">MARK DELAVERI</div>
  <div class="contact">
    <div class="contact-line"><svg class="icon"><use href="#i-home-sky"/></svg>Byblos - Lebanon, P.O.Box 48-216 Jbeil</div>
    <div class="contact-line"><svg class="icon"><use href="#i-phone-sky"/></svg>00961 71 538209 <svg class="icon"><use href="#i-mail-sky"/></svg>me@markdelaveri.com</div>
  </div>
</section>

<!-- Business card back -->
<section class="sheet card-back">
  <div class="emblem emblem--solid" style="left:102px;top:40px;width:90px;height:90px;font-size:26px">MD</div>
  <div class="web">www.markdelaveri.com</div>
</section>

<!-- Business card front -->
<section class="sheet card-front">
  <div class="wordmark">MARK DELAVERI</div>
  <div class="holder">
    <div class="holder-name">Mark Delaveri</div>
    <div class="holder-role">Consultant</div>
  </div>
  <div class="contact stack-right">
    <div class="contact-line">Byblos - Lebanon <svg class="icon"><use href="#i-home-sky"/></svg></div>
    <div class="contact-line">P.O.Box 48-216 Jbeil <svg class="icon" style="visibility:hidden"><use href="#i-home-sky"/></svg></div>
    <div class="contact-line">00961 71 538209 <svg class="icon"><use href="#i-phone-sky"/></svg></div>
    <div class="contact-line">me@markdelaveri.com <svg class="icon"><use href="#i-mail-sky"/></svg></div>
  </div>
  <div class="web">www.markdelaveri.com</div>
  <svg width="297" height="175" viewBox="0 0 297 175" style="position:absolute;left:0;top:0">
    <path d="M0 160 L297 154 V157 L0 163Z" fill="var(--sky)"/>
    <path d="M0 167 L297 161 V175 H0Z" fill="var(--sky)"/>
  </svg>
</section>

</body>
</html>
```